Anzeigengestaltung für Fliesenlegermeister
Zielgruppe
Ich bin ein Fliesenlegermeister und möchte mich selbstständig machen, ich saniere Bäder, Böden mit Fliesen, Fliesenspiegel und ich möchte eine Anzeige in den regionalen Zeitungen machen. Ich spreche alle Altersklassen mit Bädern für Sanierungen, Bodenfliesen und Neubauten an. Reparatur und Silikonarbeiten sowie Trockenbauarbeiten am eigenen Heim .
Aufgabenstellung
Ich möchte gern meine Kontaktdaten und die Farben vom Logo wieder finden,
als Beispiel habe ich meine aktuelle Visitenkarte beigefügt Dort finden sich die Kontaktdaten. Meine Arbeiten sind insbesondere :
Fliesenverlegung
Badsanierung
barrierefreie Bäder
Reparaturarbeiten
Silikonarbeiten
Trockenbau
Ob nun genau alle 6 Punkte in der Anzeige angezeigt werden soll bin ich mir nicht sicher oder ob nur 4 Beschreibungen reichen, damit es nicht zu viel wird.

```html
<!DOCTYPE html>
<html lang="de">
<head>
<meta charset="utf-8">
<title>Badsanierung – Jonas Westerkamp Fliesenlegermeister</title>
<link rel="stylesheet" href="https://fonts.googleapis.com/css2?family=Bebas+Neue&display=swap">
<style>
  :root {
    --paper: #efefef;
    --brand-blue: #1a56a0;
    --slate: #4a4a4b;
    --white: #ffffff;
  }
  html, body {
    margin: 0;
    padding: 0;
    overflow: hidden;
    background: var(--paper);
  }
  .ad {
    position: relative;
    width: 849px;
    height: 1200px;
    overflow: hidden;
    background: var(--paper);
    font-family: "Bebas Neue", "Arial Narrow", sans-serif;
  }
  .ad svg { display: block; overflow: visible; }
  .ad text { font-family: "Bebas Neue", "Arial Narrow", sans-serif; }
  .block { position: absolute; }

  .location-badge {
    left: 142px; top: 26px; width: 202px; height: 209px;
    background: var(--slate);
    clip-path: polygon(0 2%, 30% 0, 70% 1%, 100% 0, 99% 40%, 100% 100%, 60% 99%, 25% 100%, 1% 98%, 0 55%);
  }
  .brand {
    left: 382px; top: 54px; width: 320px; height: 52px;
  }
  .accessibility-note {
    left: 350px; top: 140px; width: 380px; height: 95px;
  }
  .headline-panel {
    left: 142px; top: 261px; width: 562px; height: 463px;
    background: var(--brand-blue);
    clip-path: polygon(0 1%, 40% 0, 100% 1%, 99% 50%, 100% 99%, 55% 100%, 1% 100%, 0 45%);
  }
  .services-panel {
    left: 140px; top: 745px; width: 564px; height: 162px;
    background: var(--slate);
    clip-path: polygon(0 2%, 50% 0, 100% 3%, 99% 60%, 100% 98%, 40% 100%, 1% 99%, 0 50%);
  }
  .contact-band {
    left: 142px; top: 936px; width: 578px; height: 93px;
  }
  .email-band {
    left: 140px; top: 1047px; width: 530px; height: 93px;
    background: var(--slate);
    clip-path: polygon(0 3%, 60% 0, 100% 4%, 98% 50%, 100% 97%, 45% 100%, 1% 98%, 0 40%);
  }
</style>
</head>
<body>
<main class="ad">

  <section class="block location-badge">
    <svg width="202" height="209" viewBox="0 0 202 209">
      <text x="18" y="109" fill="var(--white)" font-size="112" textLength="165" lengthAdjust="spacingAndGlyphs">NEU IN</text>
      <text x="15" y="166" fill="var(--white)" font-size="38" textLength="178" lengthAdjust="spacingAndGlyphs">BRAUNSCHWEIG</text>
    </svg>
  </section>

  <header class="block brand">
    <svg width="320" height="52" viewBox="0 0 320 52">
      <rect x="0" y="4" width="40" height="40" fill="var(--brand-blue)"/>
      <text x="52" y="30" fill="var(--brand-blue)" font-size="34" textLength="240" lengthAdjust="spacingAndGlyphs">JONAS WESTERKAMP</text>
      <text x="52" y="48" fill="var(--slate)" font-size="17" textLength="200" lengthAdjust="spacingAndGlyphs">FLIESENLEGERMEISTER</text>
    </svg>
  </header>

  <section class="block accessibility-note">
    <svg width="380" height="95" viewBox="0 0 380 95">
      <text x="15" y="42" fill="var(--slate)" font-size="52" textLength="355" lengthAdjust="spacingAndGlyphs">AUCH BARRIEREFREIER</text>
      <text x="2" y="88" fill="var(--brand-blue)" font-size="44" textLength="365" lengthAdjust="spacingAndGlyphs">UMBAU IHRES BADES MÖGLICH</text>
    </svg>
  </section>

  <section class="block headline-panel">
    <svg width="562" height="463" viewBox="0 0 562 463">
      <text x="104" y="266" fill="var(--white)" font-size="336" text-anchor="middle" textLength="92" lengthAdjust="spacingAndGlyphs">B</text>
      <text x="278" y="266" fill="var(--white)" font-size="336" text-anchor="middle" textLength="86" lengthAdjust="spacingAndGlyphs">A</text>
      <text x="414" y="266" fill="var(--white)" font-size="336" text-anchor="middle" textLength="86" lengthAdjust="spacingAndGlyphs">D</text>
      <text x="40" y="430" fill="var(--white)" font-size="225" textLength="488" lengthAdjust="spacingAndGlyphs">SANIERUNG</text>
    </svg>
  </section>

  <section class="block services-panel">
    <svg width="564" height="162" viewBox="0 0 564 162">
      <text x="14" y="45" fill="var(--white)" font-size="48" textLength="540" lengthAdjust="spacingAndGlyphs">KOMPLETTSANIERUNG | FLIESENARBEITEN</text>
      <text x="14" y="95" fill="var(--white)" font-size="48" textLength="540" lengthAdjust="spacingAndGlyphs">SILIKONARBEITEN | NEUKONZEPTION</text>
      <text x="14" y="146" fill="var(--white)" font-size="48" textLength="530" lengthAdjust="spacingAndGlyphs">REPARATUREN &amp; UMBAUTEN ALLER ART</text>
    </svg>
  </section>

  <section class="block contact-band">
    <svg width="578" height="93" viewBox="0 0 578 93">
      <polygon points="0,0 578,0 556,93 0,93" fill="var(--brand-blue)"/>
      <text x="25" y="41" fill="var(--white)" font-size="30" textLength="118" lengthAdjust="spacingAndGlyphs">JETZT TERMIN</text>
      <text x="25" y="80" fill="var(--white)" font-size="30" textLength="118" lengthAdjust="spacingAndGlyphs">VEREINBAREN</text>
      <text x="157" y="43" fill="var(--white)" font-size="36" textLength="171" lengthAdjust="spacingAndGlyphs">05307/2190475</text>
      <text x="157" y="82" fill="var(--white)" font-size="36" textLength="171" lengthAdjust="spacingAndGlyphs">0172/5501238</text>
      <text x="347" y="41" fill="var(--white)" font-size="30" textLength="150" lengthAdjust="spacingAndGlyphs">AHORNWEG 24</text>
      <text x="347" y="80" fill="var(--white)" font-size="30" textLength="185" lengthAdjust="spacingAndGlyphs">38110 BRAUNSCHWEIG</text>
    </svg>
  </section>

  <section class="block email-band">
    <svg width="530" height="93" viewBox="0 0 530 93">
      <text x="38" y="62" fill="var(--white)" font-size="42" textLength="400" lengthAdjust="spacingAndGlyphs">INFO@FLIESEN-WESTERKAMP.DE</text>
    </svg>
  </section>

</main>
</body>
</html>
```